Design A Responsive Website for Our Bar/Event Center and Restaurant

We need a Responsive Word Press Website for our Bar Event Center and our Restaurant. We need 5 pages with one page being our menu with the ability for customers to place online orders for food.
We need the entire website designed, coded and deployed. We have domain names already that need to link to the website and we also have hosting so we need the website deployed at our hosting provider. Pages should include 1) About Us 2)Bar 3)Restaurant-Menus 4) Event Venue-With Calendar 5) Contact Us

Target Market(s)

Adults 21-75 in the Louisville KY area, that go to bars, night clubs, concerts and karaoke events

Industry/Entity Type

Bar-Night Club-Music- Events

Coding

Coded - Design and coding required

Number of Pages Required

5+ page

Other font styles liked:
• Use a Font like in our logos

Colors
EE7325
F08F49
F5BC92
FAE3D3
FDF4ED
EB3D1F
EC4F4E
F09395
F8D3D4
FCEDEE

Requirements
Must have
• Online Menu Ordering with Shopping Cart, An Updateable Event Calendar, A page for posting past event pictures and videos, Ability to sell Event tickets
Nice to have
• Ability to live stream events to facebook
Should not have
• NA

```html
<!DOCTYPE html>
<html lang="en">
<head>
<meta charset="utf-8">
<title>Ridgeway Taphouse – Bar and Event Center</title>
<link href="https://fonts.googleapis.com/css2?family=Montserrat:wght@400;500;600;700&display=swap" rel="stylesheet">
<style>
:root{
  --orange:#e8601c;
  --orange-soft:#f08f49;
  --black:#000;
  --dark:#111;
  --text:#333;
  --muted:#666;
  --line:#e6e6e6;
  --white:#fff;
}
*{box-sizing:border-box;margin:0;padding:0}
html,body{width:1200px;height:3781px;overflow:hidden}
body{font-family:Arial,Helvetica,sans-serif;color:var(--text);background:var(--white);position:relative}

/* header */
.header{position:absolute;top:0;left:0;width:1200px;height:167px;background:var(--black);color:var(--white)}
.round-ico{position:absolute;width:56px;height:56px;border-radius:50%;background:var(--orange);display:flex;align-items:center;justify-content:center}
.cart-label{position:absolute;left:184px;top:40px;font:500 21px 'Montserrat',sans-serif}
.brand{position:absolute;left:443px;top:26px;width:292px;height:54px;display:flex;align-items:center;justify-content:center;white-space:nowrap;font:700 24px 'Montserrat',sans-serif;color:var(--orange)}
.call{position:absolute;left:961px;top:31px;font-family:'Montserrat',sans-serif}
.call small{display:block;font-size:13px;font-weight:600;color:var(--orange)}
.call b{font-size:20px;font-weight:600}
.header .rule{position:absolute;left:111px;top:106px;width:978px;height:1px;background:#333}
.nav{position:absolute;top:128px;left:0;width:1200px;display:flex;justify-content:center;gap:43px}
.nav a{color:var(--white);text-decoration:none;font:500 14px 'Montserrat',sans-serif;padding-bottom:10px}
.nav a.active{color:var(--orange);border-bottom:2px solid var(--orange)}

/* hero */
.hero{position:absolute;top:167px;left:0;width:1200px;height:689px;background:radial-gradient(ellipse at 50% 60%,#5a4636 0%,#2a2520 45%,#141618 100%)}
.hero-box{position:absolute;left:261px;top:186px;width:707px;height:327px;background:rgba(40,40,40,.55);text-align:center;color:var(--white)}
.hero-box h1{font:700 90px 'Montserrat',sans-serif;margin-top:14px;line-height:1.1}
.hero-box p{font:500 24px 'Montserrat',sans-serif;line-height:37px;margin-top:10px}
.btn{display:inline-flex;align-items:center;justify-content:center;background:var(--orange);color:var(--white);font-family:'Montserrat',sans-serif;font-weight:600;border-radius:30px;text-transform:uppercase}
.hero-box .btn{width:172px;height:56px;font-size:17px;margin-top:20px}
.dots{position:absolute;top:659px;left:576px;display:flex;gap:8px}
.dots i{width:11px;height:11px;border-radius:50%;background:var(--white)}
.dots i.on{background:var(--orange)}

/* section titles */
.sec-title{position:absolute;left:0;width:1200px;text-align:center;font:500 32px 'Montserrat',sans-serif;color:#333}
.bar-u{position:absolute;height:3px;width:42px;background:var(--orange)}

/* menu */
.tab{position:absolute;top:968px;width:164px;height:41px;display:flex;align-items:center;justify-content:center;font:600 13px 'Montserrat',sans-serif;border:1px solid #999;color:#555}
.tab.on{background:var(--orange);border-color:var(--orange);color:var(--white)}
.card{position:absolute;width:470px;height:156px;border:1px solid var(--line);border-radius:8px;box-shadow:0 0 6px rgba(0,0,0,.06)}
.card .ph{position:absolute;left:9px;top:9px;width:145px;height:137px;border-radius:6px}
.card h3{position:absolute;left:181px;top:26px;font:500 16px 'Montserrat',sans-serif;color:#222}
.card p{position:absolute;left:181px;top:56px;width:275px;font-size:13px;line-height:24px;color:var(--muted)}
.card .price{position:absolute;left:182px;top:110px;font:500 15px 'Montserrat',sans-serif;color:var(--orange)}

/* events */
.events{position:absolute;top:1663px;left:0;width:1200px;height:565px;background:linear-gradient(90deg,#e35e1b,#ea6a26 60%,#e35e1b)}
.cal{position:absolute;left:111px;top:72px;width:556px;height:427px;background:var(--white);border-radius:3px;box-shadow:0 0 10px rgba(0,0,0,.2)}
.cal .yr{position:absolute;top:43px;font:400 14px 'Montserrat',sans-serif;color:#999}
.cal .mo{position:absolute;left:0;width:556px;top:36px;text-align:center;font:600 21px 'Montserrat',sans-serif;color:var(--orange)}
.cal .grid{position:absolute;left:56px;top:112px;width:455px;display:grid;grid-template-columns:repeat(7,1fr);row-gap:17px;text-align:center;font:500 11px 'Montserrat',sans-serif;color:#222}
.cal .grid .dn{font-size:15px;margin-bottom:12px}
.cal .grid .sel span{display:inline-block;width:22px;height:22px;line-height:22px;margin-top:-5px;border-radius:50%;background:var(--orange);color:var(--white)}
.cal .arr{position:absolute;top:225px;width:14px;height:14px}
.cal .sbtn{position:absolute;top:360px;height:32px;display:flex;align-items:center;justify-content:center;gap:8px;font:500 11px 'Montserrat',sans-serif;color:var(--white)}
.ev-title{position:absolute;left:715px;top:82px;font:600 31px 'Montserrat',sans-serif;color:var(--white)}
.ev{position:absolute;left:715px;width:375px;color:var(--white)}
.ev .date{position:absolute;left:0;top:0;width:86px;height:86px;border:2px solid var(--white);border-radius:50%;text-align:center;font-family:'Montserrat',sans-serif}
.ev .date b{display:block;font-size:29px;font-weight:500;margin-top:14px;line-height:28px}
.ev .date small{font-size:17px}
.ev p{position:absolute;left:105px;top:22px;width:270px;font:600 16px/24px 'Montserrat',sans-serif}
.ev-sep{position:absolute;left:715px;top:279px;width:375px;height:1px;background:rgba(255,255,255,.35)}
.tickets{position:absolute;left:719px;top:432px;width:222px;height:52px;border:1px solid var(--white);border-radius:30px;display:flex;align-items:center;justify-content:center;font:600 16px 'Montserrat',sans-serif;color:var(--white)}

/* about */
.about-h{position:absolute;left:111px;top:2310px;font:600 36px 'Montserrat',sans-serif;color:#333}
.about-text{position:absolute;left:111px;top:2390px;width:469px;font-size:13px;line-height:26.6px;color:#444;text-align:justify}
.about-text p+p{margin-top:26px}
.about .btn{position:absolute;left:112px;top:2785px;width:155px;height:52px;font-size:16px}
.about-ph{position:absolute;left:644px;top:2302px;width:436px;height:540px;border-radius:6px;background:radial-gradient(ellipse at 45% 40%,#8a6040 0%,#3a2a20 55%,#1a1412 100%)}

/* contact */
.contact{position:absolute;top:2928px;left:0;width:1200px;height:512px;background:radial-gradient(ellipse at 50% 60%,#4a3a2e 0%,#24201c 55%,#121416 100%)}
.contact h2{position:absolute;top:70px;left:0;width:1200px;text-align:center;font:500 39px 'Montserrat',sans-serif;color:var(--white)}
.field{position:absolute;background:var(--white);border-radius:3px;font-size:14px;color:#555;padding:12px 15px}
.contact .btn{position:absolute;left:509px;top:405px;width:182px;height:55px;font-size:17px}

/* footer */
.footer{position:absolute;top:3440px;left:0;width:1200px;height:341px;background:var(--dark);color:var(--white)}
.footer h4{position:absolute;top:63px;font:600 21px 'Montserrat',sans-serif}
.hours{position:absolute;left:111px;top:108px;font-size:14px;line-height:36px}
.copy{position:absolute;left:111px;top:243px;font-size:14px}
.ci{position:absolute;left:474px;width:300px}
.ci .circ{position:absolute;left:0;top:0;width:44px;height:44px;border:1px solid var(--white);border-radius:50%;display:flex;align-items:center;justify-content:center}
.ci b{position:absolute;left:57px;top:0;font:600 17px 'Montserrat',sans-serif}
.ci span{position:absolute;left:57px;top:25px;font-size:13px;line-height:19px;width:220px}
.wing{position:absolute;left:792px;top:80px;width:280px;height:70px;display:flex;align-items:center;justify-content:center;white-space:nowrap;font:700 24px 'Montserrat',sans-serif;color:var(--orange)}
.social{position:absolute;left:835px;top:207px;display:flex;gap:7px}
.social i{width:36px;height:36px;border:1px solid var(--white);border-radius:50%}
</style>
</head>
<body>

<header class="header">
  <div class="round-ico" style="left:113px;top:26px">
    <svg width="24" height="24" viewBox="0 0 24 24" fill="#fff"><path d="M2 4h3l3 10h10l3-7H7" stroke="#fff" stroke-width="2" fill="none"/><circle cx="9" cy="19" r="2"/><circle cx="17" cy="19" r="2"/></svg>
  </div>
  <div class="cart-label">CART IS (0)</div>
  <div class="brand">Ridgeway Taphouse</div>
  <div class="round-ico" style="left:889px;top:26px">
    <svg width="22" height="22" viewBox="0 0 24 24" fill="#fff"><path d="M6.6 10.8a15 15 0 0 0 6.6 6.6l2.2-2.2a1 1 0 0 1 1-.25 11.4 11.4 0 0 0 3.6.57 1 1 0 0 1 1 1V20a1 1 0 0 1-1 1A17 17 0 0 1 3 4a1 1 0 0 1 1-1h3.5a1 1 0 0 1 1 1c0 1.25.2 2.45.57 3.6a1 1 0 0 1-.25 1z"/></svg>
  </div>
  <div class="call"><small>CALL US :</small><b>502-555-0147</b></div>
  <div class="rule"></div>
  <nav class="nav">
    <a class="active">HOME</a><a>ABOUT US</a><a>BAR</a><a>RESTAURANT-MENUS</a><a>EVENT VENUE-WITH CALENDAR</a><a>CONTACT US</a>
  </nav>
</header>

<section class="hero" role="img" aria-label="Photo of a dim restaurant dining room with set tables and wine glasses">
  <div class="hero-box">
    <h1>RIDGEWAY</h1>
    <p>Sed ut perspiciatis unde omnis iste natus error<br>sit voluptatem accusantium</p>
    <span class="btn">Read More</span>
  </div>
  <div class="dots"><i></i><i class="on"></i><i></i></div>
</section>

<h2 class="sec-title" style="top:897px">OUR MENU</h2>
<div class="bar-u" style="left:579px;top:946px"></div>
<div class="tab on" style="left:430px">RESTAURANT</div>
<div class="tab" style="left:606px">BAR</div>

<div class="card" style="left:110px;top:1077px"><div class="ph" role="img" aria-label="Photo of a grilled steak plate" style="background:linear-gradient(135deg,#c9b9a9,#6a3a22)"></div><h3>SED UT PERSPICIATIS UNDE</h3><p>Nemo enim ipsam voluptatem quia voluptas sit aspernatur aut odit aut fugit sed</p><span class="price">$25.00</span></div>
<div class="card" style="left:618px;top:1077px"><div class="ph" role="img" aria-label="Photo of a plated dish being served" style="background:linear-gradient(135deg,#4a6a7a,#7a3a2a)"></div><h3>SED UT PERSPICIATIS UNDE</h3><p>Nemo enim ipsam voluptatem quia voluptas sit aspernatur aut odit aut fugit sed</p><span class="price">$25.00</span></div>
<div class="card" style="left:110px;top:1251px"><div class="ph" role="img" aria-label="Photo of a fine dining plate" style="background:linear-gradient(135deg,#e8ecd8,#b07a50)"></div><h3>SED UT PERSPICIATIS UNDE</h3><p>Nemo enim ipsam voluptatem quia voluptas sit aspernatur aut odit aut fugit sed</p><span class="price">$25.00</span></div>
<div class="card" style="left:618px;top:1251px"><div class="ph" role="img" aria-label="Photo of assorted bowls of food" style="background:linear-gradient(135deg,#2a3a2a,#c08040)"></div><h3>SED UT PERSPICIATIS UNDE</h3><p>Nemo enim ipsam voluptatem quia voluptas sit aspernatur aut odit aut fugit sed</p><span class="price">$25.00</span></div>
<div class="card" style="left:110px;top:1425px"><div class="ph" role="img" aria-label="Photo of a pasta dish" style="background:linear-gradient(135deg,#1a1a1a,#b05a20)"></div><h3>SED UT PERSPICIATIS UNDE</h3><p>Nemo enim ipsam voluptatem quia voluptas sit aspernatur aut odit aut fugit sed</p><span class="price">$25.00</span></div>
<div class="card" style="left:618px;top:1425px"><div class="ph" role="img" aria-label="Photo of a chicken salad bowl" style="background:linear-gradient(135deg,#d8dcd8,#8aa060)"></div><h3>SED UT PERSPICIATIS UNDE</h3><p>Nemo enim ipsam voluptatem quia voluptas sit aspernatur aut odit aut fugit sed</p><span class="price">$25.00</span></div>

<section class="events">
  <div class="cal">
    <span class="yr" style="left:63px">2021</span>
    <div class="mo">SEPTEMBER, 2022</div>
    <span class="yr" style="left:462px">2023</span>
    <div class="grid">
      <div class="dn">SUN</div><div class="dn">MON</div><div class="dn">TUE</div><div class="dn">WED</div><div class="dn">THUR</div><div class="dn">FRI</div><div class="dn">SAT</div>
      <div>1</div><div>2</div><div>3</div><div>4</div><div>5</div><div>6</div><div>7</div>
      <div>8</div><div class="sel"><span>9</span></div><div>10</div><div>11</div><div>12</div><div>13</div><div>14</div>
      <div>15</div><div>16</div><div>17</div><div>18</div><div>19</div><div>20</div><div>21</div>
      <div>22</div><div>23</div><div>24</div><div>25</div><div>26</div><div>27</div><div>28</div>
      <div>29</div><div>30</div><div>31</div>
    </div>
    <svg class="arr" style="left:38px" viewBox="0 0 14 14"><circle cx="7" cy="7" r="6" fill="none" stroke="#555"/><path d="M8 4L5 7l3 3" stroke="#555" fill="none"/></svg>
    <svg class="arr" style="left:511px" viewBox="0 0 14 14"><circle cx="7" cy="7" r="6" fill="none" stroke="#555"/><path d="M6 4l3 3-3 3" stroke="#555" fill="none"/></svg>
    <div class="sbtn" style="left:117px;width:177px;background:var(--orange)">SEE PLANNED EVENTS <svg width="10" height="10" viewBox="0 0 10 10"><circle cx="4" cy="4" r="3" stroke="#fff" stroke-width="1.5" fill="none"/><path d="M6 6l3 3" stroke="#fff" stroke-width="1.5"/></svg></div>
    <div class="sbtn" style="left:308px;width:131px;background:#9a8a80">SET REMINDER <svg width="10" height="10" viewBox="0 0 10 10"><circle cx="5" cy="5" r="4.5" fill="#fff"/><path d="M4 3l2 2-2 2" stroke="#9a8a80" fill="none"/></svg></div>
  </div>
  <h2 class="ev-title">UPCOMING EVENTS</h2>
  <div class="bar-u" style="left:716px;top:129px;background:#fff;width:54px"></div>
  <div class="ev" style="top:171px"><div class="date"><b>25</b><small>OCT</small></div><p>Sed ut perspiciatis unde omnis natus error sit voluptatem</p></div>
  <div class="ev-sep"></div>
  <div class="ev" style="top:310px"><div class="date"><b>25</b><small>OCT</small></div><p>Sed ut perspiciatis unde omnis natus error sit voluptatem</p></div>
  <div class="tickets">BUY EVENT TICKETS</div>
</section>

<section class="about">
  <h2 class="about-h">ABOUT US</h2>
  <div class="bar-u" style="left:112px;top:2362px"></div>
  <div class="about-text">
    <p>Ridgeway Taphouse Bar and Event Center is exactly that. It’s a bar / night club on the east side of town located at 4120 Harbor Lane, just off Harbor Parkway. Easily accessible 2 minutes from the Route 9 exit, Ridgeway is your favorite neighborhood bar that you’ve never been to. Our crowd welcomes everyone but tends to lean to ages 30 and up. With our friendly hometown atmosphere, you will find that everyone knows your name. Ridgeway has 5000 sq/ft of indoor space in two separate suites each able to accommodate 100 guests. Come in to Ridgeway to enjoy our great bar food menu featuring appetizers, burgers, brats and wraps or order from Ridgeway Wing Hall our 24 Sauce Wing Buffet open 11am-7pm Monday-Friday!</p>
    <p>After you finish dinner, enjoy a beer or a cocktail while listening to a band or sing karaoke. We have karaoke 4 nights per week- Wednesday-Saturday starting at 8pm and live bands most Saturdays from 9pm-1am.</p>
  </div>
  <span class="btn">Read More</span>
  <div class="about-ph" role="img" aria-label="Photo of friends toasting with wine glasses over dinner"></div>
</section>

<section class="contact" role="img" aria-label="Photo of a dim restaurant dining room as background">
  <h2>CONTACT US</h2>
  <div class="bar-u" style="left:579px;top:124px"></div>
  <div class="field" style="left:307px;top:162px;width:287px;height:39px">First Name :</div>
  <div class="field" style="left:606px;top:162px;width:287px;height:39px">Last Name :</div>
  <div class="field" style="left:307px;top:214px;width:287px;height:39px">Email :</div>
  <div class="field" style="left:606px;top:214px;width:287px;height:39px">Phone :</div>
  <div class="field" style="left:307px;top:267px;width:589px;height:109px">Message :</div>
  <span class="btn">Submit</span>
</section>

<footer class="footer">
  <h4 style="left:111px">HOURS</h4>
  <div class="hours">Monday-Thursday 11am-11pm (or later!)<br>Friday &amp; Saturday 11am-3am<br>Sunday Noon-11pm (or later!)</div>
  <div class="copy">© Copyright 2022.All Rights Reserved</div>
  <h4 style="left:482px">CONTACT INFO</h4>
  <div class="ci" style="top:105px"><div class="circ"><svg width="14" height="18" viewBox="0 0 14 18"><path d="M7 0a7 7 0 0 0-7 7c0 5 7 11 7 11s7-6 7-11a7 7 0 0 0-7-7z" fill="#fff"/><circle cx="7" cy="7" r="2.5" fill="#111"/></svg></div><b>ADDRESS</b><span>4120 Harbor Lane Fairview,<br>KY 40299</span></div>
  <div class="ci" style="top:185px"><div class="circ"><svg width="16" height="16" viewBox="0 0 24 24" fill="#fff"><path d="M6.6 10.8a15 15 0 0 0 6.6 6.6l2.2-2.2a1 1 0 0 1 1-.25 11.4 11.4 0 0 0 3.6.57 1 1 0 0 1 1 1V20a1 1 0 0 1-1 1A17 17 0 0 1 3 4a1 1 0 0 1 1-1h3.5a1 1 0 0 1 1 1c0 1.25.2 2.45.57 3.6a1 1 0 0 1-.25 1z"/></svg></div><b>PHONE</b><span>502-555-0147</span></div>
  <div class="ci" style="top:253px"><div class="circ"><svg width="16" height="12" viewBox="0 0 16 12"><rect width="16" height="12" rx="1" fill="#fff"/><path d="M0 0l8 6 8-6" stroke="#111" fill="none"/></svg></div><b>EMAIL</b><span>orders@ridgewaytaphouse.com</span></div>
  <div class="wing">Ridgeway Wing Hall</div>
  <div class="social"><i></i><i></i><i></i><i></i><i></i></div>
</footer>

</body>
</html>
```